Design a beautiful book cover for my self help book

The Craft of Hush is a book I've written about how I learnt to quite my mind, rid myself of old pain and stand in my intuition. It's one simple practical tool to find you moment and step into your abundance. We need a cover that reflects this amazing concept! The current cover is attached. It's too dark and not in tune with the market. Please search books with similar content and make design similar yet different.

Target Market(s)

People into self help or motivational content. As well as people suffering from depression, stress, anxiety etc.

Industry/Entity Type

Self Help

Requirements
Must have
• A light airy feel of freedom
Nice to have
• Some sort of linage from current cover
Should not have
• Dark, ambiguous,

```html
<!DOCTYPE html>
<html lang="en">
<head>
<meta charset="utf-8">
<title>The Craft of Hush — Book Cover</title>
<link rel="stylesheet" href="https://fonts.googleapis.com/css2?family=Cinzel:wght@400&family=Great+Vibes&display=swap">
<style>
  :root {
    --backdrop: #000000;
    --title-blue: #1b4c80;
    --mist-white: #fbfdff;
    --mist-pale: #e2ecf4;
    --mist-soft: #c6d8e6;
    --mist-mid: #a9c2d7;
    --mist-deep: #89a8c3;
    --mist-shade: #7393b1;
    --author-white: #ffffff;
  }
  * { margin: 0; padding: 0; box-sizing: border-box; }
  html, body {
    width: 1200px;
    height: 1200px;
    overflow: hidden;
    background: var(--backdrop);
  }
  .canvas {
    position: relative;
    width: 1200px;
    height: 1200px;
    background: var(--backdrop);
  }
  .cover {
    position: absolute;
    left: 252px;
    top: 78px;
    width: 696px;
    height: 1044px;
    overflow: hidden;
  }
  .cover-artwork {
    position: absolute;
    inset: 0;
    width: 100%;
    height: 100%;
  }
  .title {
    position: absolute;
    inset: 0;
    font-weight: 400;
    color: var(--title-blue);
    text-align: center;
  }
  .title-line {
    position: absolute;
    left: 0;
    width: 100%;
    line-height: 1;
    font-weight: 400;
    white-space: nowrap;
  }
  .title-line--lead {
    top: 260px;
    font-family: "Cinzel", serif;
    font-size: 82px;
    letter-spacing: 0;
  }
  .title-line--joiner {
    top: 417px;
    font-family: "Cinzel", serif;
    font-size: 76px;
  }
  .title-line--script {
    top: 565px;
    font-family: "Great Vibes", cursive;
    font-size: 175px;
  }
  .author {
    position: absolute;
    left: 0;
    top: 936px;
    width: 100%;
    text-align: center;
    font-family: "Cinzel", serif;
    font-size: 64px;
    font-weight: 400;
    line-height: 1;
    letter-spacing: 3px;
    white-space: nowrap;
    color: var(--author-white);
    text-shadow: 1px 2px 3px rgba(25, 55, 90, 0.75), 0 0 10px rgba(40, 75, 110, 0.35);
  }
</style>
</head>
<body>
  <main class="canvas">
    <section class="cover">
      <svg class="cover-artwork" viewBox="0 0 696 1044" preserveAspectRatio="none" role="img" aria-label="Soft watercolour illustration of pale blue leafy branches framing a misty white light above a swirling pool of water">
        <defs>
          <linearGradient id="base-wash" x1="0" y1="0" x2="0" y2="1">
            <stop offset="0" stop-color="var(--mist-pale)"/>
            <stop offset="0.45" stop-color="var(--mist-soft)"/>
            <stop offset="0.75" stop-color="var(--mist-mid)"/>
            <stop offset="1" stop-color="var(--mist-shade)"/>
          </linearGradient>
          <radialGradient id="light-glow" cx="0.5" cy="0.38" r="0.5">
            <stop offset="0" stop-color="var(--mist-white)"/>
            <stop offset="0.55" stop-color="var(--mist-white)" stop-opacity="0.9"/>
            <stop offset="1" stop-color="var(--mist-white)" stop-opacity="0"/>
          </radialGradient>
          <radialGradient id="corner-tint" r="0.5">
            <stop offset="0" stop-color="var(--mist-deep)" stop-opacity="0.75"/>
            <stop offset="1" stop-color="var(--mist-deep)" stop-opacity="0"/>
          </radialGradient>
          <radialGradient id="pool-sheen" r="0.5">
            <stop offset="0" stop-color="var(--mist-white)" stop-opacity="0.75"/>
            <stop offset="1" stop-color="var(--mist-white)" stop-opacity="0"/>
          </radialGradient>
        </defs>
        <rect width="696" height="1044" fill="url(#base-wash)"/>
        <ellipse cx="40" cy="260" rx="230" ry="300" fill="url(#corner-tint)"/>
        <ellipse cx="680" cy="330" rx="220" ry="320" fill="url(#corner-tint)"/>
        <ellipse cx="60" cy="900" rx="260" ry="220" fill="url(#corner-tint)"/>
        <ellipse cx="660" cy="930" rx="260" ry="220" fill="url(#corner-tint)"/>
        <ellipse cx="348" cy="400" rx="420" ry="520" fill="url(#light-glow)"/>
        <ellipse cx="330" cy="760" rx="300" ry="110" fill="url(#pool-sheen)"/>
      </svg>

      <h1 class="title">
        <span class="title-line title-line--lead">THE CRAFT</span>
        <span class="title-line title-line--joiner">OF</span>
        <span class="title-line title-line--script">Hush</span>
      </h1>

      <p class="author">ROWAN ELLERY</p>
    </section>
  </main>
</body>
</html>
```